Online Psychiatry business - Business Card

I need a business card design. The target audience is busy professionals of any field (this therapy appeals best to 24-35 year olds). It involves psychiatry by tele-medicine (or video-conference). Nothing on it should be a giveaway that it's about mental health. Professional design with silver or gold as the primary colors appeals to me. The card must be as simple and as uncluttered as possible. Some color and flowing design on the edge of the card appeals to me.
CrestMindLink.com should probably appear in the center of the card and stand out, i.e. bold lettering, and easy to read, no cursive, but Ariel Black. Some where below this, should appear "Too Busy to Take Care of Yourself? Think again." Since this isn't office based, I don't think an office address is necessary and limits clutter.
Information that does need to appear is my name: Gerald Whitcombe, MD
General phone number: 541-876-2209. I'm hoping to get an 24-hour answering service soon so leave a little room for this. In addition I want to include two email addresses:
CrestMindLink@maildrop-box.com and CrestMind247@maildrop-box.com
Updates

I like the designs. I would like someone to put the website in bold in the center

 as most have been doing with a smaller font reminder nearby saying "No time" etc.
but I'd like to put my name down in the corner with the rest of the contact material.
Black print against a white or grey background appeals to me, with darker silver artwork near the sides (simple abstract, like wavy lines or something you can one up with that works. 
thanks

I ve tried to provide as much feedback as possible given my time limits, so if you have extra questions, please feel free to email. I tried to attach a file of a business card I really like but make be difficult to actually manufacture. I'm going to send you a link to the photo. The card has a pull tab. There is not much information on the outside. In fact, if you were to design the outside, I would just print : Too Busy to Take Care of Yourself? Think Again.

When you pull the tab the remaining information is on the bottom half of the card. Please don't use the color pink!!!!
http://www.layoutgallerypost.com/2009/05/100-clever-card-ideas/
It is the 39th photo on the list, about 2/3ds of the way down the page. It is titled: Faltenkästli

#7 and #16 have an appeal to me, except for the dot patterns
Hope this helps

I'm running out of time and energy. I 've been trying to give do down the list and give  individual feedback but I won't be able to do that anymore.

So if you have any specific questions, write me, and again thank you for all your effort!!

I know i received your files, including your zip files, Plonix,

but Gideon, did you send me the files including ZIP on project 5914386?
thanks

Target Market(s)

Working professionals and executive, attorneys, etc.

Industry/Entity Type

Business

Logo Text

Don't Have Time to Take Care of Yourself? Think Again.

Logo styles of interest
Pictorial/Combination Logo
Wordmark Logo
Other font styles liked:
• Ariel Black appeals to me the most

Requirements
Must have
• Want to emphasize that the website must be obvious, easily found (The CrestMindLink.com)
For that reason i'd like the card to be white, and minimal decoration on one or both sides just to add some style and color
Nice to have
• A Very uncluttered, elegant design, and something that makes it stick in your head-doesn't everyone want the last?
Should not have
• Nothing on the card that give it away that this is about psychiatry, such as brain or other symbol, but also nothing that gives it away as a medical business, such as a stethoscope or red cross or anything.

```html
<!DOCTYPE html>
<html lang="en">
<head>
<meta charset="utf-8">
<title>CrestMindLink – Business Card</title>
<link rel="stylesheet" href="https://fonts.googleapis.com/css2?family=Questrial&display=swap">
<style>
  :root {
    --page-bg: #f1f1f1;
    --steel-dark: #2b2d2f;
    --steel-mid: #4b4e51;
    --silver-light: #eef0f1;
    --silver-mid: #c9cccf;
    --charcoal: #3c3c3c;
    --edge-blue: #a9bcc4;
    --gold: #b89a3e;
    --gold-text: #6e5c2e;
    --ink: #1f1f1f;
    --white: #ffffff;
    --url-light: #c9cbcd;
  }
  * { margin: 0; padding: 0; box-sizing: border-box; }
  html, body {
    width: 1200px; height: 1000px; overflow: hidden;
    background: var(--page-bg);
    font-family: "Questrial", "Century Gothic", sans-serif;
  }
  .canvas { position: relative; width: 1200px; height: 1000px; }

  .card { position: absolute; left: 249px; width: 702px; height: 410px; overflow: hidden; }

  /* Front */
  .card--front {
    top: 76px;
    background:
      radial-gradient(ellipse 55% 60% at 50% 65%, rgba(255,255,255,.14), rgba(255,255,255,0) 70%),
      repeating-linear-gradient(0deg, rgba(255,255,255,.025) 0 1px, rgba(0,0,0,.03) 1px 3px),
      linear-gradient(180deg, var(--steel-dark), var(--steel-mid) 55%, var(--steel-dark));
  }
  .front__band {
    position: absolute; left: 50px; top: 131px; width: 602px; height: 30px;
    background: linear-gradient(90deg, rgba(184,154,62,0), var(--gold) 12%, var(--gold) 88%, rgba(184,154,62,0));
  }
  .front__question {
    position: absolute; left: 0; right: 0; top: 135px; text-align: center;
    font-size: 20px; letter-spacing: 2.2px; color: #3a3a34;
  }
  .front__headline {
    position: absolute; left: 0; right: 0; top: 160px; text-align: center;
    font-size: 66px; letter-spacing: 1px; color: #3c3e40;
    text-shadow: 0 1px 0 rgba(255,255,255,.25), 0 -1px 0 rgba(0,0,0,.6);
  }
  .front__url {
    position: absolute; left: 0; right: 0; top: 245px; text-align: center;
    font-size: 20px; letter-spacing: 3.4px; color: var(--url-light);
  }

  /* Back */
  .card--back {
    top: 516px;
    background:
      repeating-linear-gradient(0deg, rgba(255,255,255,.18) 0 1px, rgba(0,0,0,.025) 1px 3px),
      linear-gradient(160deg, var(--silver-mid), var(--silver-light) 45%, var(--silver-mid));
  }
  .back__wave { position: absolute; inset: 0; }
  .back__name {
    position: absolute; left: 34px; top: 40px;
    font-size: 28px; color: var(--ink); letter-spacing: .5px;
  }
  .back__url {
    position: absolute; left: 34px; top: 77px;
    font-size: 20px; color: var(--gold-text);
  }
  .back__email {
    position: absolute; left: 34px; top: 148px;
    font-size: 20px; line-height: 30px; color: var(--gold-text);
  }
  .back__email .label { color: var(--ink); }
  .back__email .indent { padding-left: 22px; }
  .back__phone {
    position: absolute; left: 470px; display: flex; align-items: center; gap: 10px;
    font-size: 23px; color: var(--white); letter-spacing: .5px;
  }
  .back__phone--main { top: 293px; }
  .back__phone--allday { top: 342px; }
  .back__phone svg { width: 30px; height: 30px; }
</style>
</head>
<body>
<div class="canvas">

  <section class="card card--front">
    <div class="front__band"></div>
    <p class="front__question">NO TIME TO TAKE CARE OF YOURSELF?</p>
    <h1 class="front__headline">THINK AGAIN</h1>
    <p class="front__url">www.crestmindlink.com</p>
  </section>

  <section class="card card--back">
    <svg class="back__wave" viewBox="0 0 702 410" preserveAspectRatio="none">
      <path d="M0 368 C 250 372, 520 280, 702 128 L702 410 L0 410 Z" fill="var(--charcoal)"/>
      <path d="M0 365 C 250 369, 520 277, 702 125" fill="none" stroke="var(--edge-blue)" stroke-width="6"/>
    </svg>
    <h2 class="back__name">GERALD WHITCOMBE, MD</h2>
    <p class="back__url">www.crestmindlink.com</p>
    <p class="back__email">
      <span class="label">E:</span> CrestMindLink@maildrop-box.com<br>
      <span class="indent">CrestMind247@maildrop-box.com</span>
    </p>
    <div class="back__phone back__phone--main">
      <svg viewBox="0 0 30 30" aria-hidden="true">
        <path d="M9 4 L13 9 L10.5 12 C12 16 14 18 18 19.5 L21 17 L26 21 L23 26 C14 26 4 16 4 7 Z" fill="var(--white)"/>
      </svg>
      <span>541.876.2209</span>
    </div>
    <div class="back__phone back__phone--allday">
      <svg viewBox="0 0 30 30" aria-hidden="true">
        <circle cx="15" cy="15" r="13" fill="none" stroke="var(--white)" stroke-width="1.5" stroke-dasharray="5 2"/>
        <path d="M8 8 L10.5 11 L9 13 C10 15 11 16 13 17 L15 15.5 L18 18 L16 21 C11 21 6 16 6 10 Z" fill="var(--white)"/>
        <text x="15" y="14" font-size="7" fill="var(--white)" font-family="Questrial, sans-serif">24</text>
        <text x="20" y="21" font-size="6" fill="var(--white)" font-family="Questrial, sans-serif">/7</text>
      </svg>
      <span>541.876.2209</span>
    </div>
  </section>

</div>
</body>
</html>
```